Compelling Home Page for Clip Harbor Partners

We are a Video SEO specialist that get websites on top of the front page of Zentrova and FlickBarn with video thumbprints that generate great traffic. Video SEO is all we do

see what we're offering at a salespage www.plumfieldreels.example. However, please omit "guarantee"

he home page should introduce our company as a premier company for helping brands get their videos on the front page of zentrova and high up in flickbarn. Should incorporate video "thumbnails" as part of the design. These could be the "triangular click buttons" or little video screens you see as "thumbnails" Needs a prominent place for a video about videoSEO. on Left side of page towards the top.

Needs buttons across the top for other pages. See www.brastonclips.example for frame of reference we want to be better than them.

Must incorporate our logo. We'd like to see the logo on dark background as well as white background.

Simple but with bright and vibrant highlights that look sophisticated, cutting edge and accountable. Shows credentials. Links with examples of thumbnails that are on the front page

We want to beat www.brastonclips.example check it out for point of reference

Target Market(s)

large corporations who have videos already and want to get better traction. Marlow 500. Advertising Agencies for Marlow 500's

Requirements
Must have
• Incorporate our logo. clean, easy to read

```html
<!DOCTYPE html>
<html lang="en">
<head>
<meta charset="utf-8">
<title>Clip Harbor Partners — Home</title>
<link rel="stylesheet" href="https://fonts.googleapis.com/css2?family=Fjalla+One&family=Oswald:wght@400;500&family=Open+Sans:wght@700&display=swap">
<style>
  :root {
    --brand-blue: #1a8cf5;
    --brand-blue-dark: #0f6fd0;
    --band-light: #a9cbe6;
    --band-mid: #7fb0da;
    --panel-blue: #8fb7de;
    --ink: #111111;
    --white: #ffffff;
    --logo-black: #050505;
    --rule-blue: #9cc3e4;
  }
  * { box-sizing: border-box; margin: 0; padding: 0; }
  html, body { width: 1200px; height: 900px; overflow: hidden; background: var(--white); }
  .page { position: relative; width: 1200px; height: 900px; font-family: "Fjalla One", sans-serif; color: var(--ink); }

  .brand-mark {
    position: absolute; display: flex; align-items: center; gap: 18px;
    background: var(--logo-black); color: var(--white);
    font-family: "Fjalla One", sans-serif;
  }
  .brand-mark .dot { border-radius: 50%; background: var(--brand-blue); flex: none; }
  .header-logo { left: 584px; top: 10px; width: 616px; height: 132px; border: 6px solid var(--brand-blue); padding-left: 36px; font-size: 46px; }
  .header-logo .dot { width: 70px; height: 70px; }
  .content-logo { left: 14px; top: 300px; width: 328px; height: 62px; padding-left: 14px; gap: 10px; font-size: 25px; }
  .content-logo .dot { width: 36px; height: 36px; }

  .nav-band {
    position: absolute; left: 0; top: 152px; width: 1200px; height: 104px;
    background: linear-gradient(180deg, var(--band-light) 0 18px, var(--band-mid) 18px 86px, var(--band-light) 86px);
  }
  .nav-rule { position: absolute; left: 0; top: 262px; width: 1200px; height: 4px; background: var(--rule-blue); }
  .nav-button {
    position: absolute; top: 16px; height: 72px;
    display: flex; align-items: center; justify-content: center;
    background: var(--brand-blue); color: var(--white);
    border: 4px solid var(--white); box-shadow: 0 0 8px rgba(0,70,160,.6);
    font-family: "Oswald", sans-serif; font-weight: 500; font-size: 36px; text-decoration: none;
  }

  .video-player { position: absolute; left: 20px; top: 392px; width: 312px; height: 228px; }
  .video-screen { width: 312px; height: 206px; border: 2px solid #cfcfcf; border-radius: 6px; background: var(--white); }

  .intro {
    position: absolute; left: 384px; top: 292px; width: 490px;
    font-size: 25px; line-height: 36.5px;
  }
  .intro p + p { margin-top: 6px; }

  .login-panel {
    position: absolute; left: 888px; top: 264px; width: 302px; height: 428px;
    background: var(--panel-blue); color: var(--white); padding: 10px 20px;
    font-family: "Open Sans", sans-serif; font-weight: 700;
  }
  .login-panel h2 { font-size: 30px; line-height: 36px; letter-spacing: 1px; }
  .login-panel label { display: block; font-size: 22px; line-height: 30px; margin-top: 10px; }
  .login-panel label + label { margin-top: 16px; }
  .login-panel .field { display: block; width: 262px; height: 44px; background: var(--white); border: 0; margin-top: 8px; }
  .login-button {
    display: inline-block; margin-top: 20px; padding: 2px 14px;
    background: var(--brand-blue); color: var(--white); border: 3px solid var(--white);
    font: 700 22px "Open Sans", sans-serif;
  }
  .new-user { margin-top: 22px; font-size: 22px; line-height: 30px; }
  .register-link { display: block; color: var(--white); font-size: 22px; line-height: 30px; margin-top: 2px; }

  .tray-rule { position: absolute; left: 0; top: 700px; width: 1200px; height: 6px; background: var(--rule-blue); }
  .tray-title {
    position: absolute; top: 716px; color: var(--brand-blue);
    font-family: "Open Sans", sans-serif; font-weight: 700; font-size: 31px;
  }
  .tray-arrow { position: absolute; top: 772px; }
  .tool-tile { position: absolute; top: 772px; width: 76px; text-align: center; }
  .tool-tile .square { display: block; width: 72px; height: 72px; margin: 0 auto; border-radius: 8px; }
  .tool-tile .name { display: block; margin-top: 4px; font: 700 14px "Open Sans", sans-serif; color: var(--brand-blue); }

  .footer-rule { position: absolute; left: 0; top: 874px; width: 1200px; height: 4px; background: var(--rule-blue); }
  .footer {
    position: absolute; left: 0; top: 878px; width: 1200px; text-align: center;
    font: 700 15px "Open Sans", sans-serif; word-spacing: 2px;
  }
  .footer span + span { margin-left: 10px; }
</style>
</head>
<body>
<div class="page">

  <div class="brand-mark header-logo"><span class="dot"></span>Clip Harbor Partners</div>

  <nav class="nav-band">
    <a class="nav-button" href="#" style="left:30px;width:166px;">Home</a>
    <a class="nav-button" href="#" style="left:260px;width:164px;">Services</a>
    <a class="nav-button" href="#" style="left:510px;width:154px;">Order</a>
    <a class="nav-button" href="#" style="left:748px;width:162px;">Examples</a>
    <a class="nav-button" href="#" style="left:1000px;width:170px;">Contact Us</a>
  </nav>
  <div class="nav-rule"></div>

  <div class="brand-mark content-logo"><span class="dot"></span>Clip Harbor Partners</div>

  <div class="video-player">
    <div class="video-screen"></div>
    <svg width="312" height="22" viewBox="0 0 312 22" aria-label="Video controls">
      <rect x="0" y="2" width="312" height="18" fill="#e6e6e6"/>
      <rect x="6" y="6" width="3" height="10" fill="#333"/><rect x="11" y="6" width="3" height="10" fill="#333"/>
      <path d="M22 6 L30 11 L22 16Z" fill="#333"/>
      <rect x="36" y="7" width="12" height="8" fill="#333"/>
      <rect x="92" y="10" width="132" height="3" fill="#bbb"/>
      <rect x="92" y="10" width="64" height="3" fill="#e02020"/>
      <circle cx="156" cy="11.5" r="4" fill="#666"/>
      <rect x="262" y="7" width="14" height="9" fill="#333"/>
      <rect x="282" y="6" width="10" height="10" fill="none" stroke="#333" stroke-width="2"/>
      <rect x="296" y="6" width="10" height="10" fill="none" stroke="#333" stroke-width="2"/>
    </svg>
  </div>

  <div class="intro">
    <p>welcome to the world of clip harbor<br>partners.our company provides you<br>find your favourate video to browse<br>this site. it willl help you to find videos</p>
    <p>easliy. welcome to the world of clip<br>harbor partners.our company provides you<br>find your favourate video to browse<br>this site. it willl help you to find videos<br>easliy.</p>
  </div>

  <form class="login-panel">
    <h2>LOGIN</h2>
    <label>User Name<span class="field"></span></label>
    <label>Password<span class="field"></span></label>
    <span class="login-button">LOGIN &gt;&gt;</span>
    <p class="new-user">New User ?</p>
    <a class="register-link" href="#">Click here to Register</a>
  </form>

  <div class="tray-rule"></div>

  <h3 class="tray-title" style="left:74px;">Videos</h3>
  <svg class="tray-arrow" style="left:14px;" width="44" height="84" viewBox="0 0 44 84" aria-label="Previous"><path d="M40 0 L0 42 L40 84Z" fill="var(--brand-blue)"/></svg>
  <svg class="tray-arrow" style="left:214px;" width="44" height="84" viewBox="0 0 44 84" aria-label="Next"><path d="M4 0 L44 42 L4 84Z" fill="var(--brand-blue)"/></svg>
  <svg style="position:absolute;left:74px;top:770px;" width="108" height="94" viewBox="0 0 108 94" aria-label="Videos">
    <rect x="2" y="2" width="104" height="90" rx="10" fill="#dcefff" stroke="#2a8ae0" stroke-width="3"/>
    <rect x="20" y="14" width="68" height="66" rx="4" fill="#2a8ae0"/>
    <rect x="34" y="20" width="40" height="24" fill="#cfe8ff"/>
    <rect x="34" y="50" width="40" height="24" fill="#cfe8ff"/>
    <g fill="#cfe8ff"><rect x="23" y="20" width="7" height="6"/><rect x="23" y="32" width="7" height="6"/><rect x="23" y="44" width="7" height="6"/><rect x="23" y="56" width="7" height="6"/><rect x="23" y="68" width="7" height="6"/><rect x="78" y="20" width="7" height="6"/><rect x="78" y="32" width="7" height="6"/><rect x="78" y="44" width="7" height="6"/><rect x="78" y="56" width="7" height="6"/><rect x="78" y="68" width="7" height="6"/></g>
  </svg>

  <h3 class="tray-title" style="left:296px;">Shopping Cart</h3>
  <svg style="position:absolute;left:344px;top:762px;" width="104" height="92" viewBox="0 0 104 92" aria-label="Shopping cart">
    <path d="M4 10 L20 10 L32 58 L88 58" fill="none" stroke="#555" stroke-width="4" stroke-linejoin="round"/>
    <path d="M22 20 L98 24 L90 50 L30 50Z" fill="none" stroke="#888" stroke-width="3"/>
    <path d="M40 22 L42 50 M58 22 L58 50 M76 23 L74 50 M26 36 L94 37" stroke="#999" stroke-width="2"/>
    <rect x="0" y="6" width="10" height="8" fill="#e03030"/>
    <circle cx="40" cy="72" r="7" fill="#e03030"/><circle cx="82" cy="72" r="7" fill="#e03030"/>
  </svg>

  <h3 class="tray-title" style="left:732px;">Uploading Tools</h3>
  <svg class="tray-arrow" style="left:558px;" width="40" height="76" viewBox="0 0 40 76" aria-label="Previous"><path d="M38 0 L0 38 L38 76Z" fill="var(--brand-blue)"/></svg>
  <svg class="tray-arrow" style="left:1128px;" width="40" height="76" viewBox="0 0 40 76" aria-label="Next"><path d="M2 0 L40 38 L2 76Z" fill="var(--brand-blue)"/></svg>

  <div class="tool-tile" style="left:626px;"><span class="square" style="background:#3b5b9a;"></span><span class="name">Friendora</span></div>
  <div class="tool-tile" style="left:726px;"><span class="square" style="background:#1d5fb4;"></span><span class="name">Spacelane</span></div>
  <div class="tool-tile" style="left:826px;"><span class="square" style="background:#c9c9d4;"></span><span class="name">Zentrova</span></div>
  <div class="tool-tile" style="left:926px;"><span class="square" style="background:#6a1e8a;"></span><span class="name">Yodelix</span></div>
  <div class="tool-tile" style="left:1026px;"><span class="square" style="background:#d8d8d8;"></span><span class="name">FlickBarn</span></div>

  <div class="footer-rule"></div>
  <footer class="footer">
    <span>Copyright your portfolio</span><span>Terms &amp; Conditions</span><span>All Rights Reserved</span><span>Privacy Policy</span>
  </footer>

</div>
</body>
</html>
```